Crestline Lending Group Business Cards

We are looking to revamp the current business cards each of our locations uses. We are a lending company that specializes in personal loans, title loans, and tax services. We have locations in New Mexico, Texas, and Oklahoma.

We would like a cleaner, sleeker look while still highlighting what we offer. Title Loans, Personal Loans & Tax Services. We also want to include our referral fee somewhere on the card. We would like to see an English option as well as a Spanish option for the cards.

PLEASE NOTE: Some business cards do not include the employee's name but just the store's location, while others will include both.

These are double-sided business cards, and we would like to see proof if possible. I have included proofs of our current business cards for you to review below, as well as our company logo. Feel free to get creative with the logo, etc! Colors should match the logo; however, you do not need to use all of our logo colors if you don't want to.

```html
<!DOCTYPE html>
<html lang="en">
<head>
<meta charset="utf-8">
<title>Crestline Lending Group – Business Cards</title>
<link href="https://fonts.googleapis.com/css2?family=Barlow:wght@400;500;700;800&family=Rubik:wght@800&display=swap" rel="stylesheet">
<style>
:root{
  --sheet:#f1f1f1;
  --card:#fafafa;
  --pattern:#f2f2f2;
  --green:#0f5130;
  --green-pattern:#0c4a2b;
  --green-soft:#1d6340;
  --red:#c1272d;
  --red-dark:#9c1d22;
  --panel:#e6e7e7;
  --ink:#2b2b2b;
  --white:#ffffff;
}
*{margin:0;padding:0;box-sizing:border-box}
html,body{width:848px;height:1200px;overflow:hidden;background:var(--sheet)}
body{position:relative;font-family:"Barlow",sans-serif;color:var(--ink)}
.card{position:absolute;overflow:hidden;box-shadow:3px 4px 6px rgba(0,0,0,.28)}
.card-light{background:var(--card)}
.card-dark{background:var(--green)}
.pattern{position:absolute;inset:0}
.card-light .pattern{background:radial-gradient(circle at 50% 50%,var(--card),var(--pattern))}
.card-dark .pattern{background:radial-gradient(circle at 50% 40%,var(--green),var(--green-pattern))}

.brand-disc{position:absolute;border-radius:50%;background:var(--panel);display:flex;flex-direction:column;align-items:center;justify-content:center;text-align:center}
.brand-disc.accent{box-shadow:3px 3px 0 var(--red)}
.brand-name{font-weight:700;color:var(--green);font-size:15px;line-height:1.05}
.brand-web{margin-top:5px;font-size:6.5px;color:var(--red);font-weight:500}

.person{position:absolute;left:0;right:0;text-align:center}
.person-name{font-weight:800;font-size:18px;color:var(--green);letter-spacing:.3px}
.person-role{font-size:10px;font-weight:500;margin-top:1px}
.state{position:absolute;left:0;right:0;text-align:center}
.state svg{display:block;margin:0 auto 3px}
.state-name{font-weight:800;font-size:18px;color:#333;letter-spacing:.5px}

.contact{position:absolute;background:var(--panel);padding:6px 0 0 11px}
.row{display:flex;align-items:center;gap:9px;margin-bottom:4px}
.ico{width:12px;height:12px;flex:none}
.phone{font-size:15px;font-weight:500;letter-spacing:.3px}
.email{font-size:10px;font-weight:500}
.addr{font-size:8.5px;line-height:1.15;font-weight:500}

.promo-brand{position:absolute;left:0;right:0;top:30px;text-align:center;color:var(--white);font-weight:700;font-size:9px}
.ribbon{position:absolute;left:50px;top:58px;width:104px;transform:rotate(-8deg);transform-origin:left top}
.ribbon-top{background:var(--white);color:var(--red);font-family:"Rubik",sans-serif;font-weight:800;font-size:10.5px;text-align:center;padding:6px 2px 3px;line-height:1}
.ribbon-bottom{background:var(--red);color:var(--white);display:flex;align-items:flex-end;justify-content:space-between;padding:2px 5px 4px}
.ribbon-small{font-family:"Rubik",sans-serif;font-weight:800;font-size:5px;margin-bottom:3px}
.ribbon-big{font-family:"Rubik",sans-serif;font-weight:800;font-size:21px;line-height:1}
.ribbon-tail{width:0;height:0;border-top:9px solid var(--red-dark);border-right:50px solid transparent}
.megaphone-area{position:absolute;left:112px;top:108px;width:62px;height:40px;background:var(--green-soft);border-radius:4px}
.services{position:absolute;left:0;right:0;top:170px;text-align:center;color:var(--white)}
.service{margin-bottom:6px}
.service-dot{width:16px;height:16px;border-radius:50%;background:var(--white);margin:0 auto 3px;display:flex;align-items:center;justify-content:center}
.service-dot span{width:6px;height:6px;border-radius:50%;background:var(--green)}
.service-name{font-size:11px;font-weight:500;letter-spacing:.3px}
</style>
</head>
<body>

<!-- English: named card -->
<section class="card card-light" style="left:202px;top:54px;width:207px;height:313px">
  <div class="pattern" role="img" aria-label="Faint pattern of finance icons: banks, safes, wallets, coins"></div>
  <div class="brand-disc accent" style="left:40px;top:26px;width:126px;height:126px">
    <div class="brand-name">Crestline<br>Lending Group</div>
    <div class="brand-web">www.crestlinelending.com</div>
  </div>
  <div class="person" style="top:169px"><div class="person-name">JANE DOE</div><div class="person-role">Branch Manager</div></div>
  <div class="contact" style="left:15px;top:224px;width:176px;height:68px">
    <div class="row"><svg class="ico" viewBox="0 0 12 12"><circle cx="6" cy="6" r="6" fill="#0f5130"/><path d="M4 3.2l1 .9-.5 1a4 4 0 002.4 2.4l1-.5.9 1-.9.8A5 5 0 013.2 4z" fill="#fff"/></svg><span class="phone">(575) 304-8862</span></div>
    <div class="row"><svg class="ico" viewBox="0 0 12 12"><circle cx="6" cy="6" r="6" fill="#0f5130"/><rect x="3" y="4" width="6" height="4.2" fill="#fff"/><path d="M3 4l3 2.3L9 4" stroke="#0f5130" stroke-width=".7" fill="none"/></svg><span class="email">hello@crestlinelending.com</span></div>
    <div class="row"><svg class="ico" viewBox="0 0 12 12"><circle cx="6" cy="6" r="6" fill="#0f5130"/><path d="M6 9.5L3.8 5.8a2.3 2.3 0 114.4 0z" fill="#fff"/><circle cx="6" cy="5" r=".8" fill="#0f5130"/></svg><span class="addr">48 Juniper Avenue, Suite C, Riverton,<br>Texas 75001</span></div>
  </div>
</section>

<!-- English: promo back -->
<section class="card card-dark" style="left:464px;top:54px;width:209px;height:313px">
  <div class="pattern" role="img" aria-label="Dark green pattern of finance icons"></div>
  <div class="promo-brand">Crestline Lending Group</div>
  <div class="ribbon">
    <div class="ribbon-top">REFER A FRIEND</div>
    <div class="ribbon-bottom"><span class="ribbon-small">Get up to</span><span class="ribbon-big">100$</span></div>
    <div class="ribbon-tail"></div>
  </div>
  <div class="megaphone-area" role="img" aria-label="Megaphone illustration announcing the referral reward"></div>
  <div class="services">
    <div class="service"><div class="service-dot"><span></span></div><div class="service-name">Title Loans</div></div>
    <div class="service"><div class="service-dot"><span></span></div><div class="service-name">Personal Loans</div></div>
    <div class="service"><div class="service-dot"><span></span></div><div class="service-name">Tax Services</div></div>
  </div>
</section>

<!-- Spanish: named card -->
<section class="card card-light" style="left:202px;top:414px;width:207px;height:314px">
  <div class="pattern" role="img" aria-label="Faint pattern of finance icons: banks, safes, wallets, coins"></div>
  <div class="brand-disc accent" style="left:40px;top:26px;width:126px;height:126px">
    <div class="brand-name">Crestline<br>Lending Group</div>
    <div class="brand-web">www.crestlinelending.com</div>
  </div>
  <div class="person" style="top:169px"><div class="person-name">JANE DOE</div><div class="person-role">Gerente de Sucursal</div></div>
  <div class="contact" style="left:15px;top:224px;width:176px;height:68px">
    <div class="row"><svg class="ico" viewBox="0 0 12 12"><circle cx="6" cy="6" r="6" fill="#0f5130"/><path d="M4 3.2l1 .9-.5 1a4 4 0 002.4 2.4l1-.5.9 1-.9.8A5 5 0 013.2 4z" fill="#fff"/></svg><span class="phone">(575) 304-8862</span></div>
    <div class="row"><svg class="ico" viewBox="0 0 12 12"><circle cx="6" cy="6" r="6" fill="#0f5130"/><rect x="3" y="4" width="6" height="4.2" fill="#fff"/><path d="M3 4l3 2.3L9 4" stroke="#0f5130" stroke-width=".7" fill="none"/></svg><span class="email">hello@crestlinelending.com</span></div>
    <div class="row"><svg class="ico" viewBox="0 0 12 12"><circle cx="6" cy="6" r="6" fill="#0f5130"/><path d="M6 9.5L3.8 5.8a2.3 2.3 0 114.4 0z" fill="#fff"/><circle cx="6" cy="5" r=".8" fill="#0f5130"/></svg><span class="addr">48 Avenida Juniper, Suite C, Riverton,<br>Texas 75001</span></div>
  </div>
</section>

<!-- Spanish: promo back -->
<section class="card card-dark" style="left:465px;top:414px;width:207px;height:314px">
  <div class="pattern" role="img" aria-label="Dark green pattern of finance icons"></div>
  <div class="promo-brand">Crestline Lending Group</div>
  <div class="ribbon">
    <div class="ribbon-top">Recomienda a<br>un Amigo</div>
    <div class="ribbon-bottom"><span class="ribbon-small">y obtén hasta</span><span class="ribbon-big">100$</span></div>
    <div class="ribbon-tail"></div>
  </div>
  <div class="megaphone-area" role="img" aria-label="Megaphone illustration announcing the referral reward" style="top:112px"></div>
  <div class="services">
    <div class="service"><div class="service-dot"><span></span></div><div class="service-name">Préstamos sobre Títulos</div></div>
    <div class="service"><div class="service-dot"><span></span></div><div class="service-name">Préstamos Personales</div></div>
    <div class="service"><div class="service-dot"><span></span></div><div class="service-name">Servicios de Impuestos</div></div>
  </div>
</section>

<!-- Location cards -->
<section class="card card-light" style="left:42px;top:780px;width:215px;height:323px">
  <div class="pattern" role="img" aria-label="Faint pattern of finance icons"></div>
  <div class="brand-disc" style="left:42px;top:26px;width:130px;height:130px"><div class="brand-name">Crestline<br>Lending Group</div><div class="brand-web">www.crestlinelending.com</div></div>
  <div class="state" style="top:179px"><svg width="12" height="16" viewBox="0 0 12 16"><path d="M6 16L1 8a5.5 5.5 0 1110 0z" fill="#0f5130"/><circle cx="6" cy="5.5" r="2.2" fill="#fafafa"/></svg><div class="state-name">NEW MEXICO</div></div>
  <div class="contact" style="left:23px;top:241px;width:168px;height:52px;padding-top:8px">
    <div class="row"><svg class="ico" viewBox="0 0 12 12"><circle cx="6" cy="6" r="6" fill="#0f5130"/><path d="M4 3.2l1 .9-.5 1a4 4 0 002.4 2.4l1-.5.9 1-.9.8A5 5 0 013.2 4z" fill="#fff"/></svg><span class="phone">(575) 304-8862</span></div>
    <div class="row"><svg class="ico" viewBox="0 0 12 12"><circle cx="6" cy="6" r="6" fill="#0f5130"/><rect x="3" y="4" width="6" height="4.2" fill="#fff"/><path d="M3 4l3 2.3L9 4" stroke="#0f5130" stroke-width=".7" fill="none"/></svg><span class="email">hello@crestlinelending.com</span></div>
  </div>
</section>

<section class="card card-light" style="left:317px;top:780px;width:215px;height:323px">
  <div class="pattern" role="img" aria-label="Faint pattern of finance icons"></div>
  <div class="brand-disc" style="left:42px;top:26px;width:130px;height:130px"><div class="brand-name">Crestline<br>Lending Group</div><div class="brand-web">www.crestlinelending.com</div></div>
  <div class="state" style="top:179px"><svg width="12" height="16" viewBox="0 0 12 16"><path d="M6 16L1 8a5.5 5.5 0 1110 0z" fill="#0f5130"/><circle cx="6" cy="5.5" r="2.2" fill="#fafafa"/></svg><div class="state-name">TEXAS</div></div>
  <div class="contact" style="left:23px;top:241px;width:168px;height:52px;padding-top:8px">
    <div class="row"><svg class="ico" viewBox="0 0 12 12"><circle cx="6" cy="6" r="6" fill="#0f5130"/><path d="M4 3.2l1 .9-.5 1a4 4 0 002.4 2.4l1-.5.9 1-.9.8A5 5 0 013.2 4z" fill="#fff"/></svg><span class="phone">(575) 304-8862</span></div>
    <div class="row"><svg class="ico" viewBox="0 0 12 12"><circle cx="6" cy="6" r="6" fill="#0f5130"/><rect x="3" y="4" width="6" height="4.2" fill="#fff"/><path d="M3 4l3 2.3L9 4" stroke="#0f5130" stroke-width=".7" fill="none"/></svg><span class="email">hello@crestlinelending.com</span></div>
  </div>
</section>

<section class="card card-light" style="left:591px;top:780px;width:215px;height:323px">
  <div class="pattern" role="img" aria-label="Faint pattern of finance icons"></div>
  <div class="brand-disc" style="left:42px;top:26px;width:130px;height:130px"><div class="brand-name">Crestline<br>Lending Group</div><div class="brand-web">www.crestlinelending.com</div></div>
  <div class="state" style="top:179px"><svg width="12" height="16" viewBox="0 0 12 16"><path d="M6 16L1 8a5.5 5.5 0 1110 0z" fill="#0f5130"/><circle cx="6" cy="5.5" r="2.2" fill="#fafafa"/></svg><div class="state-name">OKLAHOMA</div></div>
  <div class="contact" style="left:23px;top:241px;width:168px;height:52px;padding-top:8px">
    <div class="row"><svg class="ico" viewBox="0 0 12 12"><circle cx="6" cy="6" r="6" fill="#0f5130"/><path d="M4 3.2l1 .9-.5 1a4 4 0 002.4 2.4l1-.5.9 1-.9.8A5 5 0 013.2 4z" fill="#fff"/></svg><span class="phone">(575) 304-8862</span></div>
    <div class="row"><svg class="ico" viewBox="0 0 12 12"><circle cx="6" cy="6" r="6" fill="#0f5130"/><rect x="3" y="4" width="6" height="4.2" fill="#fff"/><path d="M3 4l3 2.3L9 4" stroke="#0f5130" stroke-width=".7" fill="none"/></svg><span class="email">hello@crestlinelending.com</span></div>
  </div>
</section>

</body>
</html>
```